I need a website built for my organization.
We are the world's largest network of music producers.
The website should be professional, sharp, and high quality., We need a website built for The Halvern Sound Guild. We are one of the World's largest association of music producers.
The site must be professional, sharp, and high quality., I need a website built for my organization.
The site must be professional, sharp, and high quality.
Somewhere in the top half of the site there should be a form for the user to fill out. The details of the form are as follows:
Title (large and bold): Contact Us or Submit Your Music
Fields to include (* = required): First Name*, Last Name*, Age, Zip Code, Email Address*, Daytime Phone, Evening Phone, Comments
Then, there will be a "submit" button to proceed to next step of form. Just below the "submit" button, should be the following verbiage: "After submitting, you will have the opportunity to upload demos of your music (optional) and provide other pertinent information about yourself, band, or group."
Target Market(s)
Music producers and aspiring musicians
Industry/Entity Type
Group
Colors
Designer to choose colors to be used in the design.
Look and feel

```html
<!DOCTYPE html>
<html lang="en">
<head>
<meta charset="utf-8">
<title>The Halvern Sound Guild</title>
<link href="https://fonts.googleapis.com/css2?family=Philosopher:ital,wght@0,400;0,700;1,400&family=Josefin+Sans:ital,wght@0,400;0,600;1,400&display=swap" rel="stylesheet">
<style>
:root{
  --black:#000;
  --bar:#1e1e1e;
  --panel:#1b1b1b;
  --gold:#c9a13b;
  --gold-light:#e2c26a;
  --gold-dark:#6e5012;
  --footer:#6b4e12;
  --white:#fff;
  --muted:#cfcfcf;
  --ink:#222;
}
*{box-sizing:border-box;margin:0;padding:0}
html,body{width:768px;height:1200px;overflow:hidden;background:var(--black)}
body{position:relative;font-family:"Josefin Sans",sans-serif;color:var(--white)}
.abs{position:absolute}

/* wordmark: one font, one weight, one colour */
.wordmark{font-family:"Josefin Sans",sans-serif;font-weight:600;color:var(--white);text-transform:none;letter-spacing:0}

/* header */
.topbar{left:0;top:0;width:768px;height:62px;background:var(--bar)}
.brand{left:84px;top:22px;font-size:15px;line-height:17px}
.nav{left:274px;top:42px;display:flex;font-family:"Philosopher",sans-serif;font-size:8.5px;text-transform:uppercase}
.nav a{color:var(--white);text-decoration:none;padding:6px 7px}
.nav a.current{background:var(--gold);color:var(--ink)}
.account{left:595px;top:8px;display:flex;gap:8px}
.pill{font-size:8px;padding:2px 7px;border-radius:8px;font-weight:600}
.pill.signup{background:var(--gold);color:var(--ink)}
.pill.login{background:#d8d8d8;color:var(--ink)}
.search{left:586px;top:38px;width:100px;height:15px;background:var(--white);color:#666;font-size:8px;font-style:italic;padding:3px 5px}
.search svg{position:absolute;right:4px;top:3px}

/* hero */
.hero{left:84px;top:62px;width:668px;height:204px;background:linear-gradient(135deg,#2a3448 0%,#4b5a78 40%,#2b2f3a 75%,#0d0d0d 100%)}

/* events */
.events-tab{left:98px;top:281px;width:79px;height:23px;background:var(--white);color:var(--ink);font-family:"Philosopher",sans-serif;font-weight:700;font-size:13px;text-align:center;line-height:24px}
.events{left:84px;top:304px;width:600px;height:113px;background:var(--panel)}
.arrow{top:340px;width:14px;height:40px}
.event{top:316px;width:170px}
.event h3{font-family:"Philosopher",sans-serif;color:var(--gold);font-size:13px;font-weight:400;margin-left:38px}
.event .date{position:absolute;left:0;top:30px;width:30px;height:30px;background:var(--gold);color:var(--ink);font-size:8px;text-align:center;line-height:10px;padding-top:5px;font-weight:600}
.event p{margin:5px 0 0 38px;font-size:7px;line-height:10px;text-transform:uppercase;text-align:justify;color:var(--white)}

/* form */
.form-title{left:98px;top:424px;font-family:"Philosopher",sans-serif;font-weight:700;font-size:15px}
.form-title em{font-style:normal;color:var(--gold)}
.field{height:21px;background:var(--white);color:#777;font-size:8.5px;font-style:italic;text-align:center;line-height:22px;text-transform:uppercase}
.field.area{height:50px;line-height:50px}
.figure{left:490px;top:424px;width:194px;height:105px;background:radial-gradient(ellipse at 50% 40%,#3a2a08 0%,#120d03 60%,#000 100%)}
.figure-brand{left:490px;top:530px;width:194px;text-align:center;font-size:11px;line-height:13px}
.submit{left:493px;top:560px;width:190px;height:37px;background:var(--gold-dark);font-family:"Philosopher",sans-serif;font-weight:700;font-size:21px;text-align:center;line-height:38px;color:var(--white)}
.form-note{left:84px;top:607px;width:600px;text-align:center;white-space:nowrap;font-size:5.6px;color:var(--gold);text-transform:uppercase;font-weight:600}

/* tabs */
.tab{top:624px;height:55px;font-family:"Philosopher",sans-serif;font-size:14px;text-align:center;line-height:17px;text-transform:uppercase;padding-top:9px}
.tab.gold{background:linear-gradient(180deg,var(--gold-dark) 0%,var(--gold) 55%,var(--gold-light) 100%);color:var(--white)}
.tab.active{background:var(--black);color:var(--white)}
.tab-pointer{left:372px;top:678px}
.panel{left:84px;top:679px;width:600px;height:138px;background:var(--white);color:var(--ink);text-align:center}
.panel h2{font-family:"Philosopher",sans-serif;color:var(--gold-dark);font-size:14.5px;line-height:21px;margin:20px auto 0;width:440px}
.panel p{font-size:7.6px;line-height:21px;text-transform:uppercase;margin:4px auto 0;width:540px}
.panel p em{font-style:normal;color:var(--gold)}

/* lower */
.col-title{top:838px;font-family:"Philosopher",sans-serif;font-size:14px;text-transform:uppercase}
.col-title em{font-style:normal;color:var(--gold)}
.news{left:97px;width:180px}
.news-item{position:absolute;left:0;width:180px;font-size:7.6px;line-height:17px;text-transform:uppercase;text-align:justify}
.news-item b{float:left;background:var(--gold-dark);color:var(--white);font-weight:600;padding:0 7px;margin-right:28px;line-height:15px}
.dl{left:295px;width:180px}
.dl-item{position:absolute;left:0;width:172px;height:52px;border-bottom:1px dotted var(--gold)}
.dl-item i{position:absolute;left:0;top:2px;font-style:normal;color:var(--gold);font-size:9px}
.dl-item u{position:absolute;left:26px;top:3px;font-size:7.6px;text-transform:uppercase}
.dl-item span{position:absolute;left:48px;top:21px;font-family:"Philosopher",sans-serif;color:var(--gold);font-size:11px;font-weight:700}
.photo{left:492px;top:892px;width:53px;height:77px;background:linear-gradient(180deg,#7aa0b0,#3d5560);border:2px solid var(--white)}
.quote{left:550px;top:862px;width:134px;font-size:7.1px;line-height:15.6px;font-style:italic;text-transform:uppercase;text-align:justify}
.q-name{left:550px;top:1028px;font-size:7.6px;line-height:12px;color:var(--gold);text-transform:uppercase}
.rule{top:1074px;height:2px;background:var(--muted)}
.more{top:1080px;font-size:7.6px;color:var(--gold);text-transform:uppercase}

/* footer */
.footer{left:0;top:1111px;width:768px;height:89px;background:var(--footer)}
.footer-brand{left:104px;top:1142px;font-size:12px;line-height:14px}
.footer-nav{left:265px;top:1153px;display:flex;gap:10px;font-size:7px;text-transform:uppercase}
.copy{left:360px;top:1166px;font-size:6.5px}
.follow{left:549px;top:1152px;font-family:"Philosopher",sans-serif;font-weight:700;font-size:9px}
.social{top:1148px;width:15px;height:15px;border-radius:50%;background:var(--white)}
</style>
</head>
<body>

<header>
  <div class="abs topbar"></div>
  <div class="abs brand wordmark">The Halvern<br>Sound Guild</div>
  <nav class="abs nav">
    <a class="current">Home</a><a>About Us</a><a>Event &amp; News</a><a>How to Join</a><a>Contact Us</a>
  </nav>
  <div class="abs account"><span class="pill signup">SIGN UP</span><span class="pill login">LOGIN</span></div>
  <div class="abs search">Search
    <svg width="9" height="9" viewBox="0 0 10 10"><circle cx="4" cy="4" r="3" fill="none" stroke="#333" stroke-width="1.3"/><line x1="6.3" y1="6.3" x2="9.5" y2="9.5" stroke="#333" stroke-width="1.5"/></svg>
  </div>
</header>

<div class="abs hero" role="img" aria-label="Photo of a producer's hand on a studio mixing console with headphones resting on top"></div>

<section>
  <div class="abs events-tab">EVENTS</div>
  <div class="abs events"></div>
  <svg class="abs arrow" style="left:88px" viewBox="0 0 14 40"><polyline points="11,2 3,20 11,38" fill="none" stroke="#ccc" stroke-width="3"/></svg>
  <svg class="abs arrow" style="left:666px" viewBox="0 0 14 40"><polyline points="3,2 11,20 3,38" fill="none" stroke="#ccc" stroke-width="3"/></svg>

  <div class="abs event" style="left:112px"><h3>OUR FESTIVAL</h3><div class="date">14<br>FEB</div><p>Lorem ipsum is simply dummy text of the printing and typesetting industry. Lorem ipsum has been the industry's standard dummy text ever since the 1500s</p></div>
  <div class="abs event" style="left:297px"><h3>OUR FESTIVAL</h3><div class="date">14<br>FEB</div><p>Lorem ipsum is simply dummy text of the printing and typesetting industry. Lorem ipsum has been the industry's standard dummy text ever since the 1500s</p></div>
  <div class="abs event" style="left:494px"><h3>OUR FESTIVAL</h3><div class="date">14<br>FEB</div><p>Lorem ipsum is simply dummy text of the printing and typesetting industry. Lorem ipsum has been the industry's standard dummy text ever since the 1500s</p></div>
</section>

<section>
  <h2 class="abs form-title">SUBMIT <em>MUSIC DEMO</em></h2>
  <div class="abs field" style="left:98px;top:449px;width:179px">First Name</div>
  <div class="abs field" style="left:296px;top:449px;width:179px">Email Address</div>
  <div class="abs field" style="left:98px;top:481px;width:179px">Last Name</div>
  <div class="abs field" style="left:296px;top:481px;width:179px">Daytime Phone</div>
  <div class="abs field" style="left:98px;top:514px;width:55px">Age</div>
  <div class="abs field" style="left:168px;top:514px;width:109px">Zip Code</div>
  <div class="abs field" style="left:296px;top:514px;width:179px">Evening Phone</div>
  <div class="abs field area" style="left:98px;top:546px;width:377px">Comments</div>

  <div class="abs figure" role="img" aria-label="Gold line illustration of a listener wearing headphones holding a music player"></div>
  <div class="abs figure-brand wordmark">The Halvern Sound Guild</div>
  <div class="abs submit">SUBMIT</div>
  <p class="abs form-note">After submitting, you will have the opportunity to upload demos of your music (optional) and provide other pertinent information about yourself, band, or group</p>
</section>

<section>
  <div class="abs tab gold" style="left:84px;width:208px">Who<br>we are</div>
  <div class="abs tab active" style="left:292px;width:182px">Offers from<br>music producers</div>
  <div class="abs tab gold" style="left:474px;width:210px">What<br>we do</div>
  <div class="abs panel">
    <h2>SUBMIT YOUR PROFILE THOUSANDS OF MUSIC PRODUCERS INSTANTLY!</h2>
    <p>Then, there will be a <em>"submit"</em> button to proceed to next step of form. Just below the <em>"submit"</em> button, should be the following verbiage: "<em>After submitting</em>, you will have the opportunity to <em>upload demos</em> of your music <em>(optional)</em> and provide other pertinent information about yourself, <em>band, or group</em>."</p>
  </div>
  <svg class="abs tab-pointer" width="20" height="10" viewBox="0 0 20 10"><polygon points="0,0 20,0 10,10" fill="#333"/></svg>
</section>

<section>
  <h3 class="abs col-title" style="left:139px">Latest <em>News</em></h3>
  <div class="abs news" style="top:862px">
    <div class="news-item" style="top:0"><b>05/04/2014</b>Lorem ipsum is simply dummy text of the printing and typesetting</div>
    <div class="news-item" style="top:53px"><b>05/04/2014</b>Lorem ipsum is simply dummy text of the printing and typesetting</div>
    <div class="news-item" style="top:105px"><b>05/04/2014</b>Lorem ipsum is simply dummy text of the printing and typesetting</div>
    <div class="news-item" style="top:158px"><b>05/04/2014</b>Lorem ipsum is simply dummy text of the printing and typesetting</div>
  </div>

  <h3 class="abs col-title" style="left:325px"><em>Top</em> Downloads</h3>
  <div class="abs dl" style="top:864px">
    <div class="dl-item" style="top:0"><i>1.</i><u>Lorem ipsum is simply dummy</u><span>BY NIGHT OWL</span></div>
    <div class="dl-item" style="top:53px"><i>2.</i><u>Lorem ipsum is simply dummy</u><span>BY NIGHT OWL</span></div>
    <div class="dl-item" style="top:105px"><i>3.</i><u>Lorem ipsum is simply dummy</u><span>BY NIGHT OWL</span></div>
    <div class="dl-item" style="top:158px;border:0"><i>4.</i><u>Lorem ipsum is simply dummy</u><span>BY NIGHT OWL</span></div>
  </div>

  <h3 class="abs col-title" style="left:518px">Our <em>Testimonial</em></h3>
  <div class="abs photo" role="img" aria-label="Portrait photo of the music producer giving the testimonial"></div>
  <p class="abs quote">Lorem ipsum is simply dummy text of the printing and typesetting industry. Lorem ipsum has been the industry's standard dummy text ever since the 1500s, when an unknown printer took a galley of type and scrambled it to make a type specimen book.</p>
  <p class="abs q-name">Name<br>(Music Producer)</p>

  <div class="abs rule" style="left:97px;width:180px"></div>
  <div class="abs rule" style="left:295px;width:180px"></div>
  <div class="abs rule" style="left:496px;width:180px"></div>
  <span class="abs more" style="left:219px">Read more...</span>
  <span class="abs more" style="left:416px">Read more...</span>
  <span class="abs more" style="left:616px">Read more...</span>
</section>

<footer>
  <div class="abs footer"></div>
  <div class="abs footer-brand wordmark">The Halvern<br>Sound Guild</div>
  <nav class="abs footer-nav"><span>Home</span><span>About Us</span><span>Event &amp; News</span><span>How to Join</span><span>Contact Us</span></nav>
  <span class="abs copy">copy-rights@reserved</span>
  <span class="abs follow">FOLLOW US:</span>
  <span class="abs social" style="left:612px" aria-label="Social network link"></span>
  <span class="abs social" style="left:637px" aria-label="Social network link"></span>
</footer>

</body>
</html>
```